Business Cards for an 'affordable luxury' inner city home builder in Calgary.

We need a business card design that emulates the progressive, innovative, culture of our company and the modern style of our homes. Use our website www.velmarcrest-ab.com as a reference for the product we build.

Our company builds homes in the inner city space of Calgary, Alberta. We build affordable luxury.

Target Market(s)

Young professional Families

Contact Information for Business Card

Try to maintain consistency with the logo font and the card font.

Requirements
Must have
• The details must include: Name, education, title, phone number, website and email (Address is not as important)
• The design must be uniques (like our logo), elegant, sophisticated and modern.

```html
<!DOCTYPE html>
<html lang="en">
<head>
<meta charset="utf-8">
<title>Velmar Crest Homes Ltd – Business Card</title>
<link href="https://fonts.googleapis.com/css2?family=Roboto:wght@400;500;700&family=Roboto+Condensed:wght@400&display=swap" rel="stylesheet">
<style>
  :root {
    --page-bg: #e4e4e4;
    --card-light: #ffffff;
    --card-dark: #232323;
    --ink: #222222;
    --ink-soft: #555555;
    --mark-grey: #7d7d7d;
    --rule: #8a8a8a;
  }
  * { margin: 0; padding: 0; box-sizing: border-box; }
  html, body { width: 1125px; height: 1200px; overflow: hidden; }
  body { background: var(--page-bg); position: relative; font-family: "Roboto", Arial, sans-serif; }

  .card {
    position: absolute;
    left: 150px;
    width: 826px;
    height: 472px;
    box-shadow: 0 3px 6px rgba(0,0,0,0.25);
  }
  .card--front { top: 98px; background: var(--card-light); }
  .card--back { top: 631px; background: var(--card-dark); }

  .brand {
    position: absolute;
    left: 82px;
    top: 222px;
    display: flex;
    align-items: center;
    gap: 14px;
  }
  .brand__square { width: 46px; height: 46px; border: 3px solid var(--ink); }
  .brand__name {
    font-size: 22px;
    font-weight: 500;
    line-height: 1.15;
    letter-spacing: 0.06em;
    color: var(--ink);
    text-transform: uppercase;
  }

  .divider {
    position: absolute;
    left: 413px;
    top: 112px;
    width: 2px;
    height: 285px;
    background: linear-gradient(to bottom, rgba(138,138,138,0), var(--rule) 15%, var(--rule) 85%, rgba(138,138,138,0));
  }

  .details { position: absolute; left: 442px; top: 108px; color: var(--ink); }
  .details__name { font-size: 31px; font-weight: 700; line-height: 1.15; margin-left: -3px; }
  .details__roles {
    list-style: none;
    font-family: "Roboto Condensed", "Arial Narrow", sans-serif;
    font-size: 18.5px;
    line-height: 25px;
    margin-top: 1px;
  }
  .details__address { font-size: 19px; color: var(--ink-soft); margin-top: 24px; }
  .contact { list-style: none; margin-top: 10px; font-size: 19px; color: var(--ink-soft); line-height: 25px; }
  .contact li { display: flex; align-items: center; gap: 9px; }
  .contact svg { width: 16px; height: 16px; fill: var(--ink); flex: none; }

  .back-brand {
    position: absolute;
    left: 0; right: 0;
    top: 160px;
    display: flex;
    justify-content: center;
    align-items: center;
    gap: 20px;
  }
  .back-brand__square { width: 70px; height: 70px; border: 5px solid var(--mark-grey); }
  .back-brand__name {
    font-size: 34px;
    font-weight: 500;
    letter-spacing: 0.08em;
    color: var(--mark-grey);
    text-transform: uppercase;
    line-height: 1.15;
  }
  .back-url {
    position: absolute;
    left: 0; right: 0;
    top: 353px;
    text-align: center;
    font-size: 19px;
    letter-spacing: 0.55em;
    color: var(--mark-grey);
  }
</style>
</head>
<body>
  <section class="card card--front">
    <div class="brand">
      <div class="brand__square"></div>
      <div class="brand__name">Velmar Crest<br>Homes Ltd</div>
    </div>
    <div class="divider"></div>
    <div class="details">
      <h1 class="details__name">Harjeet</h1>
      <ul class="details__roles">
        <li>Co-Founder</li>
        <li>Business Development / Strategy</li>
        <li>Professional Engineer (P.ENG)</li>
        <li>Masters of Business Administration (MBA)</li>
      </ul>
      <p class="details__address">418 17 Ave NE, Calgary, AB</p>
      <ul class="contact">
        <li>
          <svg viewBox="0 0 16 16" aria-hidden="true"><path d="M3.6 1.2l2.2 2.6c.3.4.3.9 0 1.3L4.7 6.4c.9 2 2.5 3.6 4.5 4.6l1.3-1.1c.4-.3.9-.3 1.3 0l2.6 2.2c.4.3.4.9.1 1.3l-1.2 1.4c-.5.5-1.2.7-1.9.5C6.2 13.9 2.3 10 .9 4.9.7 4.2.9 3.5 1.4 3L2.3 1.1c.4-.3 1-.3 1.3.1z"/></svg>
          403-555-0148
        </li>
        <li>
          <svg viewBox="0 0 16 16" aria-hidden="true"><path d="M2 4h12v.8L8 9 2 4.8z"/><path d="M2 6.2l6 4.2 6-4.2V12H2z"/></svg>
          projects@velmarcrest-ab.com
        </li>
        <li>
          <svg viewBox="0 0 16 16" aria-hidden="true"><circle cx="8" cy="8" r="7"/><path d="M5 4.5c1.5-.5 2.5.5 2 1.5s-2 .8-2 2.2 1.5 1 1.8 2.3L6.5 13c-2-1-3.2-3-3-5 .3-1.5.8-2.8 1.5-3.5zM10 3.5c1 .5.5 1.8-.3 2.3s.4 1.8 1.5 1.5 1.8.2 1.5 1.5" fill="#ffffff"/></svg>
          www.velmarcrest-ab.com
        </li>
      </ul>
    </div>
  </section>

  <section class="card card--back">
    <div class="back-brand">
      <div class="back-brand__square"></div>
      <div class="back-brand__name">Velmar Crest<br>Homes Ltd</div>
    </div>
    <p class="back-url">www.velmarcrest-ab.com</p>
  </section>
</body>
</html>
```